Ground breaking athletic gear company needs a kick ass business card

We are an American start up athletic gear company that uses a medically proven biohack to boost athletic performance. Heat kills strength and endurance. Our gear helps athletes manage heat better and ultimatley can improve them by up to 10% instantly. Nothing like it out there! Launching this summer.
We are looking for a modern, minimalist design that captures a sporty edge. Check out www.velmarunwear.com, @velmarunwear on instagram for more ideas.

Target Market(s)

25-35 year olds, male and female athletes, vaultlift athletes, competitive runners

Industry/Entity Type

Business

Contact Information for Business Card

Dorian Pellham
Founder
dorianp@velmarunwear.com
www.VelmaRunwear.com
+1 (555) 014-2286

Font styles to use
Sans Serif

Requirements
Must have
• Logo and icon
• All contact information
• dorianp@velmarunwear.com
• +1 (555) 019-4471 M
• +1 (555) 014-2286
Nice to have
• Tag line : "Cool & Conquer"

```html
<!DOCTYPE html>
<html lang="en">
<head>
<meta charset="utf-8">
<title>Velma Runwear – Business Card</title>
<link href="https://fonts.googleapis.com/css2?family=Open+Sans:wght@400;600;700&display=swap" rel="stylesheet">
<style>
  :root {
    --backdrop: #ecebe8;
    --card-dark: #262d38;
    --card-light: #f4f2f2;
    --brand-blue: #4a8fd6;
    --ink: #2b2b2e;
    --ink-soft: #4a4a4f;
    --shadow: rgba(30, 30, 40, 0.18);
  }
  * { box-sizing: border-box; margin: 0; padding: 0; }
  html, body {
    width: 1200px;
    height: 801px;
    overflow: hidden;
    background: var(--backdrop);
    font-family: "Open Sans", Arial, sans-serif;
  }
  .stage {
    position: relative;
    width: 1200px;
    height: 801px;
    display: flex;
    align-items: center;
    justify-content: center;
    gap: 40px;
  }
  .card {
    width: 540px;
    height: 309px;
    border-radius: 4px;
    box-shadow: 0 10px 28px var(--shadow);
    position: relative;
  }
  .card--front {
    background: var(--card-dark);
    display: flex;
    align-items: center;
    justify-content: center;
  }
  .card--back {
    background: var(--card-light);
    display: flex;
    align-items: center;
    padding: 0 36px 0 44px;
  }
  .wordmark {
    font-weight: 700;
    color: var(--brand-blue);
    letter-spacing: 0.12em;
    text-transform: uppercase;
    line-height: 1;
    text-align: center;
  }
  .card--front .wordmark { font-size: 40px; }
  .card--back .wordmark { font-size: 26px; text-align: left; }
  .wordmark__line { display: block; }
  .wordmark__line + .wordmark__line { margin-top: 8px; }
  .brand-block { flex: 0 0 220px; }
  .contact { flex: 1; padding-left: 22px; color: var(--ink); }
  .contact__name {
    font-size: 20px;
    font-weight: 400;
    color: var(--ink-soft);
    line-height: 1.1;
    white-space: nowrap;
  }
  .contact__name strong { font-weight: 700; color: var(--ink); }
  .contact__role {
    font-size: 13px;
    font-weight: 600;
    margin-top: 2px;
    margin-bottom: 14px;
  }
  .contact__list { list-style: none; }
  .contact__item {
    display: flex;
    align-items: center;
    gap: 10px;
    font-size: 13px;
    line-height: 1.75;
    color: var(--ink);
    white-space: nowrap;
  }
  .contact__icon { width: 14px; height: 14px; flex: 0 0 14px; }
</style>
</head>
<body>
<main class="stage">
  <section class="card card--front" aria-label="Card front">
    <div class="wordmark">
      <span class="wordmark__line">Velma</span>
      <span class="wordmark__line">Runwear</span>
    </div>
  </section>

  <section class="card card--back" aria-label="Card back">
    <div class="brand-block">
      <div class="wordmark">
        <span class="wordmark__line">Velma</span>
        <span class="wordmark__line">Runwear</span>
      </div>
    </div>
    <div class="contact">
      <p class="contact__name">Dorian <strong>Pellham</strong></p>
      <p class="contact__role">Founder</p>
      <ul class="contact__list">
        <li class="contact__item">
          <svg class="contact__icon" viewBox="0 0 14 14" aria-hidden="true">
            <rect x="0.5" y="2.5" width="13" height="9" rx="1" fill="var(--brand-blue)"/>
            <path d="M1 3.5 L7 8 L13 3.5" fill="none" stroke="#fff" stroke-width="1.2"/>
          </svg>
          dorianp@velmarunwear.com
        </li>
        <li class="contact__item">
          <svg class="contact__icon" viewBox="0 0 14 14" aria-hidden="true">
            <g fill="none" stroke="var(--brand-blue)" stroke-width="1.2">
              <circle cx="7" cy="7" r="6"/>
              <ellipse cx="7" cy="7" rx="2.6" ry="6"/>
              <line x1="1" y1="7" x2="13" y2="7"/>
              <line x1="2" y1="4" x2="12" y2="4"/>
              <line x1="2" y1="10" x2="12" y2="10"/>
            </g>
          </svg>
          www.VelmaRunwear.com
        </li>
        <li class="contact__item">
          <svg class="contact__icon" viewBox="0 0 14 14" aria-hidden="true">
            <path d="M1 5 Q7 1 13 5 L11.5 6.5 L9.5 5.5 L9.5 4.5 Q7 3.8 4.5 4.5 L4.5 5.5 L2.5 6.5 Z" fill="var(--brand-blue)"/>
            <rect x="2.5" y="7" width="9" height="6" rx="1" fill="var(--brand-blue)"/>
            <circle cx="7" cy="10" r="1.5" fill="#fff"/>
          </svg>
          +1 (555) 014-2286
        </li>
        <li class="contact__item">
          <svg class="contact__icon" viewBox="0 0 14 14" aria-hidden="true">
            <rect x="3.5" y="0.5" width="7" height="13" rx="1.2" fill="var(--brand-blue)"/>
            <rect x="4.6" y="2" width="4.8" height="8" fill="#fff"/>
            <circle cx="7" cy="11.8" r="0.8" fill="#fff"/>
          </svg>
          +1 (555) 019-4471 M
        </li>
      </ul>
    </div>
  </section>
</main>
</body>
</html>
```